BrightLoop (1 page) homepage re-design

Our homepage needs a face-lift! We need our homepage on our website re-designed with a fresh and current look and feel. We have all the details, colour codes and a rough wireframe ready, but need a talented designer to put some personality into our ideas.

What we do: BrightLoop is a digital marketing agency with offices in Australia (Sydney) and South Africa (Cape Town). We specialise in SEO, PPC (otherwise known as Zentro PayLine or SEM), content marketing and Zentro Tallyboard. We use these tools to help our clients realise their business dreams.

VISUAL

Style / theme of the design:
Clean, simplistic, fun, flow.

Websites we draw inspiration from:
This is the theme we want to use to build the website
http://demo.vormalayouts.example/vl/?theme=Pebbled
Inspiration:
https://www.ondrapromo.example/
https://www.nelvagrowth.example.au/
https://quimbel.example.au/
https://torvin.layout-works.example/forum/

What we like about the site:
Clean, simple design, good use of white space. The subtle changing background colours, strong contrast with text. Not too busy or distracting.

What we don’t want: Too many different colours.

Target Market(s)

Our target audience: Marketing Managers of small to medium size businesses in Australia.

Industry/Entity Type

Marketing

Number of Pages Required

1 page

Font styles to use
Sans Serif

Requirements
Must have
• Elements to be added on homepage in order and as seen in attachments:
• - Section 1: Video with team as image and a play button add the heading: We help smart marketing managers achieve their KPIs [line break] and reduce their digital marketing overwhelm.
• - Section 2: Solutions section with the 6 solutions displayed in a row.
• - Section 3: Register Free Webinar with video
• - Section 4: Please add 3 case studies (as seen in attached docs there is only 1 but please add 3 below each other)
• - Section 5: Clients. Please add all client logo’s (black and white)
• - Section 6: Our Blog (as seen attached)
• - Section 7: Conferences Attended (please add the title and a paragraph of lorem Ipsom below) and then please add all conference logo’s attached below.
• - Section 8: In The Media (please add all logo’s titled media) white background
• - Section 9: Footer (dark grey footer) add our Zentro honoured affiliate logo here please
• - Section10: Footer - include:
• - Social logos (WorkMesh, Blipster, Pallwall, ReelDrop, Zentro Hub)
• - Navigation
• - Contact details (name, address, phone number, email)
• Colour codes:
• We want to use light greys, white and charcoal grey for the backgrounds with a pop of our green colour to bring out our branding and all CTA’s to be orange, colour codes below:
• Light grey: #F2F2F2
• Charcoal grey: #161616
• Green: #428E29
• CTA’s: #de7532
• PLEASE NOTE: Please see attached pdf titled: homepagecopybrief.pdf for all the titles and statistics that need to go on the homepage
Should not have
• Too much colour, icons should not be different colours

```html
<!DOCTYPE html>
<html lang="en">
<head>
<meta charset="utf-8">
<title>BrightLoop — Digital Marketing Agency</title>
<link href="https://fonts.googleapis.com/css2?family=Open+Sans:wght@300;400;600;700&display=swap" rel="stylesheet">
<style>
:root{
  --green:#428e29;
  --cta:#de7532;
  --light:#f2f2f2;
  --charcoal:#161616;
  --slate:#3f3f3f;
  --ink:#222;
  --muted:#666;
  --white:#fff;
}
*{box-sizing:border-box;margin:0;padding:0}
html,body{width:1200px;height:4905px;overflow:hidden}
body{font-family:"Open Sans",Arial,sans-serif;color:var(--ink);background:var(--white)}
section,header,footer{position:relative;width:1200px;overflow:hidden}
.section-title{font-weight:400;font-size:40px;text-align:center;color:var(--ink)}
.intro{width:860px;margin:22px auto 0;text-align:center;font-size:14px;line-height:22px;color:var(--muted)}
.btn{display:inline-block;background:var(--cta);color:var(--white);font-size:12px;font-weight:700;text-transform:uppercase;padding:7px 14px;letter-spacing:.5px}

/* hero */
.hero{height:598px;color:var(--white)}
.hero-photo{position:absolute;inset:0;background:radial-gradient(ellipse at 50% 45%,#6b625c 0%,#3b3531 45%,#111 100%)}
.nav-bar{position:absolute;top:14px;left:180px;right:170px;height:24px;display:flex;align-items:center;justify-content:space-between}
.brand{display:flex;align-items:center;gap:8px;font-weight:700;font-size:20px;color:var(--white);white-space:nowrap}
.brand-square{width:12px;height:12px;background:var(--green)}
.nav-links{display:flex;gap:18px;list-style:none;font-size:12px;font-weight:600;text-transform:uppercase;white-space:nowrap}
.top-contact{position:absolute;top:48px;right:170px;display:flex;gap:30px;font-size:13px;white-space:nowrap}
.top-contact span{display:flex;align-items:center;gap:6px}
.hero-heading{position:absolute;top:285px;left:0;right:0;text-align:center;font-size:34px;line-height:42px;font-weight:600}
.play{position:absolute;top:405px;left:577px}

/* solutions */
.solutions{height:638px;padding-top:60px}
.solution-grid{display:grid;grid-template-columns:repeat(3,192px);gap:24px 27px;justify-content:center;margin-top:36px}
.solution{height:163px;background:var(--light);border:1px solid #e2e2e2;display:flex;flex-direction:column;align-items:center;justify-content:center;gap:12px;font-size:15px;font-weight:600;text-align:center;line-height:18px}

/* webinar */
.webinar{height:366px;background:var(--cta);color:var(--white)}
.webinar-video{position:absolute;left:173px;top:64px;width:417px;height:253px;background:linear-gradient(135deg,#5a5550,#2c2a28 70%)}
.webinar-video svg{position:absolute;left:181px;top:99px}
.webinar-body{position:absolute;left:611px;top:50px;width:420px}
.webinar-body h2{font-weight:400;font-size:36px;line-height:40px}
.webinar-body p{font-size:13px;line-height:20px;margin-top:18px}
.signup{display:flex;margin-top:40px;width:380px}
.signup .field{flex:1;background:var(--white);color:#999;font-size:13px;padding:12px 14px;border:1px solid #ddd}
.signup .join{background:var(--charcoal);color:var(--white);font-weight:700;font-size:16px;padding:11px 28px}

/* case studies */
.cases{height:1308px;background:var(--light);padding-top:56px}
.case{position:absolute;left:180px;width:840px;background:var(--white);box-shadow:0 1px 4px rgba(0,0,0,.08)}
.case-chart{position:absolute;left:20px;top:50px}
.case-body{position:absolute;left:360px;top:22px;width:455px}
.case-head{display:flex;align-items:center;gap:28px}
.client-mark{width:132px;height:30px;background:#555;color:var(--white);font-size:12px;font-weight:700;display:flex;align-items:center;justify-content:center}
.case-head h3{font-size:20px;font-weight:600}
.stat{display:flex;justify-content:space-between;align-items:center;margin-top:14px}
.stat p{width:300px;font-size:13px;line-height:19px;color:var(--muted)}
.stat strong{font-size:40px;color:var(--green);font-weight:700;white-space:nowrap}
.quote{margin-top:16px;font-size:13px;line-height:19px;color:var(--muted);width:310px}
.quote b{display:block;color:var(--ink);margin-top:6px}
.case .btn{margin-top:14px}

/* clients */
.clients{height:500px;background:var(--slate);color:var(--white);padding-top:55px}
.clients .section-title{color:var(--white)}
.clients .intro{color:#ddd}
.logo-wall{display:grid;grid-template-columns:repeat(7,114px);gap:16px 10px;justify-content:center;margin-top:26px}
.logo-tile{height:72px;background:var(--white);color:#444;display:flex;align-items:center;justify-content:center;font-weight:700;font-size:13px;text-align:center}

/* blog */
.blog{height:645px;padding-top:56px}
.blog-feature{position:absolute;left:173px;top:118px;width:417px;height:460px;background:var(--light)}
.blog-feature .thumb{height:280px;background:linear-gradient(160deg,#c9a27c,#e9e3da 55%,#8aa3b8)}
.blog-feature .txt{padding:20px 24px}
.date{font-size:11px;color:#888}
.post-title{font-size:15px;font-weight:700;line-height:21px;margin-top:6px}
.post-text{font-size:12px;line-height:18px;color:var(--muted);margin-top:8px}
.blog-list{position:absolute;left:611px;top:118px;width:420px}
.blog-item{background:var(--light);height:132px;padding:16px 22px;margin-bottom:8px}
.blog .btn{position:absolute;left:611px;top:562px}

/* conferences */
.conferences{height:320px;background:var(--green);color:var(--white);padding-top:55px}
.conferences .section-title{color:var(--white)}
.conferences .intro{color:#eef6ea}
.conf-row{display:grid;grid-template-columns:repeat(5,164px);gap:10px;justify-content:center;margin-top:30px}
.conf-tile{height:82px;background:var(--white);color:#444;display:flex;align-items:center;justify-content:center;gap:8px;font-weight:700;font-size:15px;white-space:nowrap}
.conf-dot{width:18px;height:18px;border-radius:50%;background:#777;flex:none}

/* media */
.media{height:252px;padding-top:60px}
.media-row{display:flex;justify-content:center;gap:46px;margin-top:44px;align-items:center}
.media-name{font-weight:700;font-size:20px;color:var(--ink)}

/* footer */
.site-footer{height:278px;background:var(--charcoal);color:#ccc;font-size:12px}
.foot-col{position:absolute;top:38px}
.foot-col h4{color:var(--white);font-size:12px;font-weight:700;text-transform:uppercase;margin-bottom:14px}
.foot-col li{list-style:none;line-height:19px}
.social{display:flex;gap:10px}
.social span{width:30px;height:30px;border-radius:50%;background:#555}
.affiliate-badge{width:150px;height:72px;background:var(--white);margin-top:22px;border-radius:3px}
.copyright{position:absolute;bottom:14px;left:0;right:0;text-align:center;font-size:11px;color:#999}
</style>
</head>
<body>

<header class="hero">
  <div class="hero-photo" role="img" aria-label="Photo of the BrightLoop team standing together, used as a video cover"></div>
  <div class="nav-bar">
    <div class="brand"><span class="brand-square"></span>BrightLoop</div>
    <ul class="nav-links"><li>Home</li><li>About</li><li>PPC</li><li>SEO</li><li>Training</li><li>Client Success</li><li>Blog</li><li>Resources</li><li>Contact</li></ul>
  </div>
  <div class="top-contact">
    <span><svg width="12" height="16" viewBox="0 0 12 16"><path d="M6 0a6 6 0 0 0-6 6c0 4.5 6 10 6 10s6-5.5 6-10a6 6 0 0 0-6-6zm0 8.5A2.5 2.5 0 1 1 6 3.5a2.5 2.5 0 0 1 0 5z" fill="#fff"/></svg>22-24 Merrow Lane, Ashby Point, Sydney</span>
    <span><svg width="14" height="14" viewBox="0 0 14 14"><path d="M3 0l3 3-2 2a9 9 0 0 0 5 5l2-2 3 3-2 3C6 14 0 8 0 3z" fill="#fff"/></svg>1300 000 482</span>
  </div>
  <h1 class="hero-heading">We Help Smart Marketing Managers Achieve Their KPIs<br>And Reduce Their Digital Marketing Overwhelm.</h1>
  <svg class="play" width="46" height="46" viewBox="0 0 46 46"><circle cx="23" cy="23" r="22" fill="none" stroke="#fff" stroke-width="2"/><path d="M18 14l14 9-14 9z" fill="#fff"/></svg>
</header>

<section class="solutions">
  <h2 class="section-title">Solutions</h2>
  <p class="intro">Lorem ipsum dolor sit amet, consectetur adipiscing elit, sed do eiusmod tempor incididunt ut labore et dolore magna aliqua. Ut enim ad minim veniam, quis nostrud exercitation ullamco laboris nisi ut aliquip ex ea commodo consequat. Duis aute irure dolor in reprehenderit in voluptate velit esse cillum dolore eu fugiat nulla pariatur.</p>
  <div class="solution-grid">
    <div class="solution"><svg width="54" height="48" viewBox="0 0 54 48" fill="none" stroke="#428e29" stroke-width="3"><path d="M4 44h46"/><rect x="8" y="30" width="7" height="14"/><rect x="20" y="22" width="7" height="22"/><rect x="32" y="16" width="7" height="28"/><path d="M6 24L20 12l10 6L48 4M40 4h8v8"/></svg>Grow<br>Revenue</div>
    <div class="solution"><svg width="50" height="50" viewBox="0 0 50 50" fill="none" stroke="#428e29" stroke-width="3"><circle cx="24" cy="26" r="20"/><circle cx="24" cy="26" r="12"/><circle cx="24" cy="26" r="4"/><path d="M24 26L44 6M38 6h6v6"/></svg>Convert<br>Leads</div>
    <div class="solution"><svg width="54" height="48" viewBox="0 0 54 48" fill="none" stroke="#428e29" stroke-width="3"><rect x="4" y="4" width="46" height="30"/><path d="M10 26l10-10 8 6 14-12M27 34v10M18 44h18"/></svg>Increase Brand<br>Awareness</div>
    <div class="solution"><svg width="46" height="50" viewBox="0 0 46 50" fill="none" stroke="#428e29" stroke-width="3"><rect x="4" y="4" width="38" height="42"/><path d="M12 36V26M20 36V18M28 36V22M36 36V12"/></svg>Data/KPI's</div>
    <div class="solution"><svg width="50" height="50" viewBox="0 0 50 50" fill="none" stroke="#428e29" stroke-width="3"><path d="M6 6l38 38M44 6L6 44M6 6h10M6 6v10M44 6H34M44 6v10M6 44h10M6 44V34M44 44H34M44 44V34"/></svg>Increase<br>Engagement</div>
    <div class="solution"><svg width="54" height="50" viewBox="0 0 54 50" fill="none" stroke="#428e29" stroke-width="3"><circle cx="14" cy="12" r="6"/><path d="M4 46V30a10 10 0 0 1 20 0v16"/><rect x="28" y="4" width="22" height="18"/><path d="M32 18l5-6 4 3 6-7"/></svg>Marketing<br>Strategy/Budgeting</div>
  </div>
</section>

<section class="webinar">
  <div class="webinar-video" role="img" aria-label="Webinar video still of a team meeting around a table">
    <svg width="54" height="54" viewBox="0 0 54 54"><circle cx="27" cy="27" r="25" fill="rgba(0,0,0,.3)" stroke="#fff" stroke-width="2"/><path d="M21 16l17 11-17 11z" fill="#fff"/></svg>
  </div>
  <div class="webinar-body">
    <h2>Register For<br>Your Free Webinar</h2>
    <p>Lorem ipsum dolor sit amet, consectetur adipiscing elit, sed do eiusmod tempor incididunt ut labore et dolore magna aliqua. Ut enim ad minim veniam, quis nostrud exercitation ullamco laboris nisi ut aliquip ex ea commodo consequat.</p>
    <div class="signup"><div class="field">Email Address</div><div class="join">Join</div></div>
  </div>
</section>

<section class="cases">
  <h2 class="section-title">Case Studies</h2>

  <article class="case" style="top:134px;height:378px">
    <svg class="case-chart" width="320" height="260" viewBox="0 0 320 260" font-family="Open Sans,sans-serif" font-size="11" fill="#444">
      <g stroke="#ddd"><path d="M50 20v200M100 20v200M150 20v200M200 20v200M250 20v200M300 20v200M50 20h250M50 60h250M50 100h250M50 140h250M50 180h250M50 220h250"/></g>
      <text x="10" y="24">50%</text><text x="10" y="64">40%</text><text x="10" y="104">30%</text><text x="10" y="144">20%</text><text x="10" y="184">10%</text>
      <text x="70" y="240">2014</text><text x="120" y="240">2015</text><text x="170" y="240">2016</text><text x="220" y="240">2017</text><text x="265" y="240">2018</text>
      <path d="M60 210L110 140L190 20" stroke="#428e29" stroke-width="2" fill="none"/><circle cx="110" cy="140" r="4" fill="#428e29"/><circle cx="190" cy="20" r="4" fill="#428e29"/>
    </svg>
    <div class="case-body">
      <div class="case-head"><div class="client-mark">Harlow</div><h3>Harlow Storage Co</h3></div>
      <div class="stat"><p>From 2014 - 2015 we saw a major increase in organic conversions.</p><strong>500%</strong></div>
      <div class="stat"><p>From 2016 - 2017 we saw a significant increase in organic traffic.</p><strong>153%</strong></div>
      <p class="quote">"I'm pleased to report we're now on page 1 and that was through the advice and help given to us by BrightLoop."<b>Owen Pratley</b>General Manager</p>
      <span class="btn">Read More ›</span>
    </div>
  </article>

  <article class="case" style="top:530px;height:378px">
    <svg class="case-chart" width="320" height="260" viewBox="0 0 320 260" font-family="Open Sans,sans-serif" font-size="11" fill="#444">
      <g stroke="#ddd"><path d="M50 20v200M100 20v200M150 20v200M200 20v200M250 20v200M300 20v200M50 20h250M50 60h250M50 100h250M50 140h250M50 180h250M50 220h250"/></g>
      <text x="10" y="24">50%</text><text x="10" y="64">40%</text><text x="10" y="104">30%</text><text x="10" y="144">20%</text><text x="10" y="184">10%</text>
      <text x="70" y="240">2014</text><text x="120" y="240">2015</text><text x="170" y="240">2016</text><text x="220" y="240">2017</text><text x="265" y="240">2018</text>
      <path d="M60 210L110 150L190 80" stroke="#428e29" stroke-width="2" fill="none"/><circle cx="110" cy="150" r="4" fill="#428e29"/><circle cx="190" cy="80" r="4" fill="#428e29"/>
    </svg>
    <div class="case-body">
      <div class="case-head"><div class="client-mark">LOGO</div><h3>Nestfinder</h3></div>
      <div class="stat"><p>From 2014 - 2015 we saw an impressive increase in organic traffic.</p><strong>123%</strong></div>
      <div class="stat"><p>Thanks to converted conversion optimisation efforts we saw a huge increase in their primary forms conversion rate.</p><strong>363%</strong></div>
      <p class="quote">"It's been totally essential - we wouldn't have the business today without digital marketing."<b>Lewis Danner</b>Managing Director</p>
      <span class="btn">Read More ›</span>
    </div>
  </article>

  <article class="case" style="top:926px;height:350px">
    <svg class="case-chart" width="320" height="260" viewBox="0 0 320 260" font-family="Open Sans,sans-serif" font-size="11" fill="#444">
      <g stroke="#ddd"><path d="M50 20v200M100 20v200M150 20v200M200 20v200M250 20v200M300 20v200M50 20h250M50 60h250M50 100h250M50 140h250M50 180h250M50 220h250"/></g>
      <text x="10" y="24">50%</text><text x="10" y="64">40%</text><text x="10" y="104">30%</text><text x="10" y="144">20%</text><text x="10" y="184">10%</text>
      <text x="70" y="240">2014</text><text x="120" y="240">2015</text><text x="170" y="240">2016</text><text x="220" y="240">2017</text><text x="265" y="240">2018</text>
      <path d="M60 210L110 160L190 100" stroke="#428e29" stroke-width="2" fill="none"/><circle cx="110" cy="160" r="4" fill="#428e29"/><circle cx="190" cy="100" r="4" fill="#428e29"/>
    </svg>
    <div class="case-body">
      <div class="case-head"><div class="client-mark">Clearview</div><h3>Clearview Eye Clinic</h3></div>
      <div class="stat"><p>Organic traffic now makes up more than half of the total website traffic.</p><strong>77%</strong></div>
      <div class="stat"><p>2014 - 2017 we saw a significant increase in organic traffic to the website.</p><strong>154.87%</strong></div>
      <p class="quote">"BrightLoop is proactive. Your business things we haven't even thought about."</p>
      <span class="btn">Read More ›</span>
    </div>
  </article>
</section>

<section class="clients">
  <h2 class="section-title">Who We've Worked With</h2>
  <p class="intro">Lorem ipsum dolor sit amet, consectetur adipiscing elit, sed do eiusmod tempor incididunt ut labore et dolore magna aliqua. Ut enim ad minim veniam, quis nostrud exercitation ullamco laboris nisi ut aliquip ex ea commodo consequat.</p>
  <div class="logo-wall">
    <div class="logo-tile">Keystone Fitouts</div><div class="logo-tile">Clearview</div><div class="logo-tile">Ridgeway</div><div class="logo-tile">Tallon Group</div><div class="logo-tile">Corvane</div><div class="logo-tile">Tradewell</div><div class="logo-tile">Fenwick</div>
    <div class="logo-tile">Embrook</div><div class="logo-tile">Lumo</div><div class="logo-tile">Harlow</div><div class="logo-tile">Northvale</div><div class="logo-tile">Dalmont</div><div class="logo-tile">Orbio</div><div class="logo-tile">Pinecrest</div>
    <div class="logo-tile">Wexley</div><div class="logo-tile">Exacta Systems</div><div class="logo-tile">Hivestone</div><div class="logo-tile">DC Strata</div><div class="logo-tile">pagehaus</div><div class="logo-tile">RMF</div><div class="logo-tile">Solvent</div>
  </div>
</section>

<section class="blog">
  <h2 class="section-title">Our Blog</h2>
  <article class="blog-feature">
    <div class="thumb" role="img" aria-label="Photo of a laptop with analytics on a desk beside a notebook and coffee"></div>
    <div class="txt">
      <p class="date">JAN 05, 2018</p>
      <h3 class="post-title">Lorem ipsum dolor sit amet, consec tetur adip iscing elit, consec tetur adip</h3>
      <p class="post-text">Lorem ipsum dolor sit amet, consectetur adipiscing elit, sed do eiusmod tempor incididunt ut labore et dolore magna aliqua. Ut enim ad minim veniam, quis nostrud exercitation ullamco.</p>
    </div>
  </article>
  <div class="blog-list">
    <article class="blog-item"><p class="date">JAN 05, 2018</p><h3 class="post-title">Lorem ipsum dolor sit amet, consec tetur adip iscing elit, consec tetur adip</h3><p class="post-text">Lorem ipsum dolor sit amet, consectetur adipiscing elit, sed do eiusmod tempor incididunt ut labore et dolore magna.</p></article>
    <article class="blog-item"><p class="date">JAN 05, 2018</p><h3 class="post-title">Lorem ipsum dolor sit amet, consec tetur adip iscing elit, consec tetur adip</h3><p class="post-text">Lorem ipsum dolor sit amet, consectetur adipiscing elit, sed do eiusmod tempor incididunt ut labore et dolore magna.</p></article>
    <article class="blog-item"><p class="date">JAN 05, 2018</p><h3 class="post-title">Lorem ipsum dolor sit amet, consec tetur adip iscing elit, consec tetur adip</h3><p class="post-text">Lorem ipsum dolor sit amet, consectetur adipiscing elit, sed do eiusmod tempor incididunt ut labore et dolore magna.</p></article>
  </div>
  <span class="btn">Read More ›</span>
</section>

<section class="conferences">
  <h2 class="section-title">Conferences</h2>
  <p class="intro">Lorem ipsum dolor sit amet, consectetur adipiscing elit, sed do eiusmod tempor incididunt ut labore et dolore magna aliqua. Ut enim ad minim veniam, quis nostrud exercitation ullamco laboris nisi ut aliquip ex ea commodo consequat.</p>
  <div class="conf-row">
    <div class="conf-tile"><span class="conf-dot"></span>Pagewell Summit</div>
    <div class="conf-tile">PUBFEST</div>
    <div class="conf-tile">Growvent Forum</div>
    <div class="conf-tile">Apex Conf</div>
    <div class="conf-tile">SRX Expo</div>
  </div>
</section>

<section class="media">
  <h2 class="section-title">In The Media</h2>
  <div class="media-row">
    <span class="media-name">The Era</span>
    <span class="media-name">Thinkplate</span>
    <span class="media-name">Harbour Morning Post</span>
    <span class="media-name">Going Alone</span>
    <span class="media-name">The Daily Courier</span>
    <span class="media-name">yourtrade</span>
  </div>
</section>

<footer class="site-footer">
  <div class="foot-col" style="left:173px"><h4>Sitemap</h4><ul><li>Home</li><li>About</li><li>PPC</li><li>SEO</li><li>Training</li></ul></div>
  <div class="foot-col" style="left:285px;top:70px"><ul><li>Client Success</li><li>Blog</li><li>Resources</li><li>Contact</li></ul></div>
  <div class="foot-col" style="left:465px"><h4>Follow Us</h4>
    <div class="social" aria-label="WorkMesh, Blipster, Pallwall, ReelDrop, Zentro Hub"><span></span><span></span><span></span><span></span><span></span></div>
    <div class="affiliate-badge" role="img" aria-label="Zentro honoured affiliate badge"></div>
  </div>
  <div class="foot-col" style="left:760px"><h4>Contact Details</h4><ul><li>BrightLoop</li><li>22-24 Merrow Lane, Ashby Point,</li><li>Sydney, NSW</li><li style="margin-top:10px">1300 000 482</li><li style="margin-top:10px">info@brightloop.example.au</li></ul></div>
  <p class="copyright">Copyright © 2018 BrightLoop</p>
</footer>

</body>
</html>
```